Junior Rugby Event needs 4 page Brochure

4 Page A4 brochure to be designed for a junior rugby event to be held in japan.. The brochure will entice coaches, teachers and players to the event.
The brochure will provide a basic overview of the event - dates, venue and promote some of the key features of the host, venue and event.
Event logo has been included. Design overview with copy has been included as word document. Images have been attached that can be used or alternatives sourced. A PDF document has been included of a design example that we like.
Target Market(s)
Rugby Clubs and Schools
Industry/Entity Type
Events
Look and feel

```html
<!DOCTYPE html>
<html lang="en">
<head>
<meta charset="utf-8">
<title>Junior Rugby Brochure – Inner Spread</title>
<link href="https://fonts.googleapis.com/css2?family=Bitter:ital,wght@0,700;0,800;1,800&family=Arimo:wght@400;700&display=swap" rel="stylesheet">
<style>
  :root {
    --navy: #1c2464;
    --ink: #1f2430;
    --backdrop: #e7ece8;
    --veil: rgba(255,255,255,0.62);
    --grass-dark: #5f7a45;
    --grass-light: #a9b896;
    --sky: #c9d0d8;
    --frame: #1c2464;
  }
  * { box-sizing: border-box; margin: 0; padding: 0; }
  html, body { width: 1200px; height: 833px; overflow: hidden; }
  body { background: var(--backdrop); font-family: "Arimo", Arial, sans-serif; color: var(--ink); }

  .spread { position: absolute; left: 40px; top: 36px; width: 1120px; height: 760px; display: flex; box-shadow: 0 10px 30px rgba(0,0,0,0.18); }
  .page { position: relative; width: 560px; height: 760px; overflow: hidden; }
  .page-bg { position: absolute; inset: 0; }
  .page--left .page-bg { background: linear-gradient(180deg, var(--sky) 0%, #9aa596 45%, var(--grass-light) 70%, var(--grass-dark) 100%); }
  .page--right .page-bg { background: linear-gradient(180deg, var(--sky) 0%, #aab3a6 40%, var(--grass-light) 68%, var(--grass-dark) 100%); }
  .page-veil { position: absolute; inset: 0; background: var(--veil); }
  .page--left .page-veil { box-shadow: inset -18px 0 24px -14px rgba(0,0,0,0.25); }
  .page--right .page-veil { box-shadow: inset 18px 0 24px -14px rgba(0,0,0,0.25); }

  .content { position: absolute; }
  .heading { font-family: "Bitter", Georgia, serif; font-weight: 800; color: var(--navy); font-size: 21px; margin-bottom: 8px; }
  .body-text { font-size: 11.6px; line-height: 1.33; color: var(--ink); }
  .body-text p + p { margin-top: 0; }

  .overview { left: 36px; top: 36px; width: 490px; }
  .signoff { margin-top: 14px; }
  .signoff-name { font-family: "Bitter", Georgia, serif; font-style: italic; font-weight: 800; color: var(--navy); font-size: 13px; text-transform: uppercase; }
  .signoff-role { font-weight: 700; font-size: 11.5px; text-transform: uppercase; color: var(--ink); }

  .venue { left: 36px; top: 318px; width: 490px; }
  .venue-copy { width: 215px; }
  .venue-photo { position: absolute; left: 240px; top: 12px; width: 250px; height: 134px; border: 3px solid var(--frame); background: linear-gradient(180deg, #2f6a4c 0%, #3c7a55 62%, #6e9a45 100%); }
  .venue-extra { margin-top: 22px; }

  .where { left: 30px; top: 36px; width: 500px; }
  .where-copy { width: 240px; }
  .photo-stack { position: absolute; left: 254px; top: 6px; width: 246px; display: flex; flex-direction: column; gap: 10px; }
  .photo { height: 126px; border: 3px solid var(--frame); }
  .photo--shrine { background: linear-gradient(180deg, #a9c3df 0%, #c2412f 55%, #8a8f94 100%); }
  .photo--street { background: linear-gradient(180deg, #15163a 0%, #b52a3a 50%, #e1b53a 100%); }
  .photo--mountain { background: linear-gradient(180deg, #b3242a 0%, #8fb5d9 45%, #e9eef2 65%, #c53a2c 100%); }

  .who { left: 30px; top: 590px; width: 500px; }
</style>
</head>
<body>
  <div class="spread">
    <section class="page page--left">
      <div class="page-bg" role="img" aria-label="Young rugby players stretching on a grass training pitch"></div>
      <div class="page-veil"></div>

      <div class="content overview">
        <h2 class="heading">Tournament Overview</h2>
        <div class="body-text">
          <p>The Pacific Youth Rugby Invitational has been created to provide a meeting point for young rugby players from across the globe as the eyes of the rugby world turn towards Japan in 2019. This event will provide a once in a lifetime experience, both on and off the field. Teams will have the opportunity to match up against international opponents and as well as taking in some of the unique culture and history of Japan.</p>
          <p>Teams will be guaranteed 4 games during the event.</p>
          <p>The tournament will feature school, club and development teams from across the Rugby World. Invitations have been sent to teams across the rugby world to Australia, New Zealand, England, Ireland, Scotland, Wales, South Africa, USA, Canada, Argentina, France, Asia and the Pacific Islands.</p>
          <p>We invite you to join us in Japan for this celebration of rugby.</p>
        </div>
        <div class="signoff">
          <p class="signoff-name">Daniel Harwood</p>
          <p class="signoff-role">Chairman – Pacific Junior Rugby Invitational</p>
        </div>
      </div>

      <div class="content venue">
        <h2 class="heading">Venue</h2>
        <div class="body-text venue-copy">
          <p>The Summit Arena is a multi purpose sports venue with 5 football fields, track and field facilities, multiple tennis courts, gymnasium, martial arts dojo, training center, conference center, restaurants and accommodation, with the main stadium seating 10,000 spectators and is the home ground of the Harbour City Blues.</p>
        </div>
        <div class="venue-photo" role="img" aria-label="Green arena building with its name on the facade above a grassy bank"></div>
        <div class="body-text venue-extra">
          <p>In addition to the fantastic sports facilities the Summit Arena has onsite accommodation in Lodges and onsite dining options including Cafeteria with seating for up to 250, Buffet Restaurant, Traditional Japanese Restaurant, Bakery and Cafe as well BBQ areas.</p>
        </div>
      </div>
    </section>

    <section class="page page--right">
      <div class="page-bg" role="img" aria-label="Rugby ball resting on a grass pitch"></div>
      <div class="page-veil"></div>

      <div class="content where">
        <h2 class="heading">Where</h2>
        <div class="body-text where-copy">
          <p>Fukuoka is the largest city on the island of Kyushu, the third largest of Japan's islands, and the sixth largest city in Japan with a population in excess of 2.5 million.</p>
          <p>As a major regional hub Fukuoka has direct flight connections from Tokyo, Osaka, Shanghai, Seoul, Bangkok, Singapore, Taipei, Hoi Chi Minh, Hong Kong and Honolulu, as well as via Shinkansen to the rest of Japan including Tokyo, Hiroshima, Kyoto and Osaka.</p>
          <p>Fukuoka City is home to one of the 2019 Rugby World Cup Venues, Fukuoka Bayside Stadium with a capacity of 22,563 built in 1995. Fukuoka Bayside Stadium will host three World Cup fixtures including France versus USA on Wednesday 2nd October 2019.</p>
          <p>Kyushu is home to two other world cup stadiums. Oita Hillside Stadium will host five games including New Zealand versus Repechage Winner on Wednesday 2nd October 2019 and Australia versus Uruguay on Saturday 5th October 2019. Kumamoto Riverside Stadium will host two games including France versus Tonga on Sunday 6th October 2019.</p>
        </div>
        <div class="photo-stack">
          <div class="photo photo--shrine" role="img" aria-label="Red shrine gate at the top of stone steps"></div>
          <div class="photo photo--street" role="img" aria-label="City street at night lit by neon signs"></div>
          <div class="photo photo--mountain" role="img" aria-label="Snow-capped mountain framed by red autumn maple leaves"></div>
        </div>
      </div>

      <div class="content who">
        <h2 class="heading">Who</h2>
        <div class="body-text">
          <p>The Tournament will feature U17, U15 &amp; U13 Categories and is open to club, school and development teams. Each age category will be seeded with the ability to play off for Plate, Bowl and Trophy divisions.</p>
        </div>
      </div>
    </section>
  </div>
</body>
</html>
```